Harborline4trades Pwrpt Design

I need a professional PWRPT template around Harborline4trades. The website associated http://harborline4trades.example/ . I have included several documents that highlight our color pallet and goals. The template will serve as a tool to tell our story as a company.
BACKGROUND: We also own QM7lr (Bridgewell Advisory 7 Learning www.qm7lr.example ). QM7lr offers research-policy-and practical solutions for educators. Our Harborline4trades was born out of one of these solutions. QM7lr (We) just launched the H4T solution.
Associated websites for reference:
http://harborline4trades.example/
http://www.qm7lr.example/

```html
<!DOCTYPE html>
<html lang="en">
<head>
<meta charset="utf-8">
<title>Harborline4trades – Title Slide</title>
<link rel="stylesheet" href="https://fonts.googleapis.com/css2?family=Carlito:wght@400;700&display=swap">
<style>
  :root {
    --orange: #f39a2b;
    --orange-light: #f8c480;
    --orange-deep: #e98a1e;
    --charcoal: #58585a;
    --ink: #1b1b1b;
    --white: #ffffff;
    --tagline: #4a4a4a;
  }
  * { margin: 0; padding: 0; box-sizing: border-box; }
  html, body { width: 1200px; height: 900px; overflow: hidden; background: var(--white); }
  .slide {
    position: relative;
    width: 1200px;
    height: 900px;
    overflow: hidden;
    font-family: "Carlito", "Calibri", sans-serif;
  }
  .hero-photo {
    position: absolute;
    left: 0; top: 0;
    width: 1200px; height: 700px;
    background:
      radial-gradient(ellipse at 30% 30%, rgba(255,255,255,0.18), transparent 55%),
      linear-gradient(160deg, var(--orange-light) 0%, var(--orange) 55%, var(--orange-deep) 100%);
  }
  .slide-title {
    position: absolute;
    left: 330px;
    top: 312px;
    font-size: 66px;
    font-weight: 400;
    color: var(--ink);
    line-height: 1;
    white-space: nowrap;
  }
  .swoosh {
    position: absolute;
    left: 0; top: 0;
    width: 1200px; height: 900px;
  }
  .brand {
    position: absolute;
    left: 0; right: 0;
    top: 760px;
    text-align: center;
  }
  .brand-name {
    font-size: 38px;
    font-weight: 400;
    color: var(--orange);
    line-height: 1;
  }
  .brand-tagline {
    margin-top: 6px;
    font-size: 19px;
    font-weight: 400;
    color: var(--tagline);
    letter-spacing: 1px;
    line-height: 1;
  }
  .footer-bar {
    position: absolute;
    left: 0; bottom: 0;
    width: 1200px; height: 38px;
    background: var(--charcoal);
  }
</style>
</head>
<body>
  <main class="slide">
    <div class="hero-photo" role="img" aria-label="Photo of an instructor leaning over to help a student writing at a desk, tinted orange"></div>
    <h1 class="slide-title">Project Title Here</h1>

    <svg class="swoosh" viewBox="0 0 1200 900" aria-hidden="true">
      <path d="M0,640 C320,535 760,505 1200,548 L1200,900 L0,900 Z" fill="var(--white)"/>
      <path d="M0,668 C330,570 780,545 1200,570 L1200,745 C880,640 420,625 0,668 Z" fill="var(--charcoal)"/>
    </svg>

    <div class="brand">
      <div class="brand-name">Harborline4trades</div>
      <div class="brand-tagline">Skills for Every Shoreline</div>
    </div>

    <div class="footer-bar"></div>
  </main>
</body>
</html>
```